Kestrel Bridge Consulting (KBC) Business Card Design

I would like to create double-sided business cards that contain:
1) Name: Derek Molvane
2) Phone Number: +1 (555) 218-4907
3) Email: Derek.Molvane@KestrelBridgeConsulting.example
4) Website: KestrelBridgeConsulting.example

I would like to include my logo and a color scheme similar to the Varnholt Grand Prix Ostera squad color scheme (black, silver, greenish-blue – but can also include regular blue)

What we do: Our company develops and delivers innovative and pragmatic information technology and cybersecurity risk and compliance solutions for organizations in the commercial market as well as the federal, and state/local sectors.

```html
<!DOCTYPE html>
<html lang="en">
<head>
<meta charset="utf-8">
<title>Kestrel Bridge Consulting – Business Card</title>
<link rel="stylesheet" href="https://fonts.googleapis.com/css2?family=Montserrat:wght@300;400;500;600&display=swap">
<style>
  :root {
    --backdrop: #0f1c1d;
    --card: #ffffff;
    --ink: #27323b;
    --ink-soft: #2f3a44;
    --teal: #33bfb7;
    --blue: #1f6fb5;
    --rule: #2a2f33;
  }
  * { box-sizing: border-box; margin: 0; padding: 0; }
  html, body {
    width: 985px; height: 1200px; overflow: hidden;
    background: var(--backdrop);
    font-family: "Montserrat", Arial, sans-serif;
  }
  .canvas { position: relative; width: 985px; height: 1200px; }
  .card {
    position: absolute; left: 171px; width: 646px; height: 395px;
    background: var(--card);
  }
  .card--front { top: 167px; }
  .card--back { top: 639px; }

  .brand { position: absolute; display: flex; align-items: center; }
  .brand__dot { border-radius: 50%; background: var(--teal); flex: none; }
  .brand__rule { background: var(--rule); flex: none; }
  .brand__name {
    color: var(--ink); font-weight: 500; text-transform: uppercase;
    line-height: 1.08; letter-spacing: 0.02em;
  }
  .card--front .brand { left: 139px; top: 149px; }
  .card--front .brand__dot { width: 96px; height: 96px; margin-right: 10px; }
  .card--front .brand__rule { width: 1.5px; height: 86px; margin-right: 9px; }
  .card--front .brand__name { font-size: 26px; }

  .card--back .brand { left: 392px; top: 36px; }
  .card--back .brand__dot { width: 54px; height: 54px; margin-right: 9px; }
  .card--back .brand__rule { width: 1px; height: 48px; margin-right: 5px; }
  .card--back .brand__name { font-size: 14.5px; }

  .person { position: absolute; left: 45px; top: 200px; }
  .person__name { font-size: 18px; font-weight: 600; color: var(--ink); letter-spacing: 0.02em; }
  .person__title { font-size: 16px; font-weight: 600; color: var(--teal); margin-top: 8px; letter-spacing: 0.03em; }

  .contacts { position: absolute; left: 45px; top: 273px; list-style: none; }
  .contacts__item {
    display: flex; align-items: center; height: 27px;
    font-size: 16.5px; font-weight: 300; color: var(--ink-soft);
  }
  .contacts__icon { width: 16px; height: 16px; margin-right: 12px; fill: var(--blue); flex: none; }
</style>
</head>
<body>
<main class="canvas">
  <section class="card card--front" aria-label="Card front">
    <div class="brand">
      <span class="brand__dot"></span>
      <span class="brand__rule"></span>
      <p class="brand__name">Kestrel<br>Bridge<br>Consulting</p>
    </div>
  </section>

  <section class="card card--back" aria-label="Card back">
    <div class="brand">
      <span class="brand__dot"></span>
      <span class="brand__rule"></span>
      <p class="brand__name">Kestrel<br>Bridge<br>Consulting</p>
    </div>

    <div class="person">
      <h1 class="person__name">DEREK MOLVANE</h1>
      <p class="person__title">CEO</p>
    </div>

    <ul class="contacts">
      <li class="contacts__item">
        <svg class="contacts__icon" viewBox="0 0 24 24" aria-hidden="true"><path d="M6.6 10.8c1.4 2.8 3.8 5.1 6.6 6.6l2.2-2.2c.3-.3.7-.4 1-.2 1.1.4 2.3.6 3.6.6.6 0 1 .4 1 1V20c0 .6-.4 1-1 1C10.6 21 3 13.4 3 4c0-.6.4-1 1-1h3.5c.6 0 1 .4 1 1 0 1.3.2 2.5.6 3.6.1.3 0 .7-.2 1z"/></svg>
        +1 (555) 218-4907
      </li>
      <li class="contacts__item">
        <svg class="contacts__icon" viewBox="0 0 24 24" aria-hidden="true"><path d="M3 6h18v12H3z" fill="none"/><path d="M3 6h18v12H3V6zm2 2v.3l7 4.4 7-4.4V8H5zm0 2.6V16h3.6L5 10.6zm14 0L15.4 16H19v-5.4zM6.8 16h10.4l-3-4.4L12 13l-2.2-1.4L6.8 16z"/></svg>
        Derek.Molvane@KestrelBridgeConsulting.example
      </li>
      <li class="contacts__item">
        <svg class="contacts__icon" viewBox="0 0 24 24" aria-hidden="true"><path d="M12 2a10 10 0 1 0 0 20 10 10 0 0 0 0-20zm6.9 6h-3a15.7 15.7 0 0 0-1.4-3.6A8 8 0 0 1 18.9 8zM12 4c.8 1.2 1.5 2.5 1.9 4h-3.8c.4-1.5 1.1-2.8 1.9-4zM4.3 14a8 8 0 0 1 0-4h3.4a16 16 0 0 0 0 4H4.3zm.8 2h3a15.7 15.7 0 0 0 1.4 3.6A8 8 0 0 1 5.1 16zm3-8h-3a8 8 0 0 1 4.4-3.6C8.9 5.5 8.4 6.7 8.1 8zM12 20c-.8-1.2-1.5-2.5-1.9-4h3.8c-.4 1.5-1.1 2.8-1.9 4zm2.3-6H9.7a14.6 14.6 0 0 1 0-4h4.6a14.6 14.6 0 0 1 0 4zm.3 5.6c.6-1.1 1.1-2.3 1.4-3.6h3a8 8 0 0 1-4.4 3.6zm1.7-5.6a16 16 0 0 0 0-4h3.4a8 8 0 0 1 0 4h-3.4z"/></svg>
        KestrelBridgeConsulting.example
      </li>
    </ul>
  </section>
</main>
</body>
</html>
```